Website Header for new website

We need a header/banner design for our revised website. Here is the link to our existing website lorimentaskel.me and to our new website in process seasonbrightway.us
Area of expertise is older adults, baby boomers and caregivers
This is an individual, professional website for a Speaker, Keynoter, Author, Brocaster

Target Market(s)

Event planners, broadcasters, publishers

Font styles to use
Serif

```html
<!DOCTYPE html>
<html lang="en">
<head>
<meta charset="utf-8">
<title>Lori Mentaskel – Speaker, Author, Broadcaster</title>
<link rel="stylesheet" href="https://fonts.googleapis.com/css2?family=Lato:wght@400;700;900&family=Roboto:wght@400;700&family=Great+Vibes&display=swap">
<style>
:root{
  --nav-bg:#34454f;
  --page-bg:#eeeeee;
  --white:#ffffff;
  --band-bg:rgba(30,34,40,.78);
  --tile-bg:rgba(255,255,255,.28);
  --tile-border:rgba(255,255,255,.45);
  --accent-blue:#2d4fc4;
  --ink:#111111;
  --body-ink:#444444;
}
*{box-sizing:border-box;margin:0;padding:0}
html,body{width:1200px;height:1200px;overflow:hidden;background:var(--page-bg)}
body{position:relative;font-family:'Lato',sans-serif;color:var(--white)}
.abs{position:absolute}

.site-nav{left:0;top:0;width:1200px;height:78px;background:var(--nav-bg)}
.brand{left:40px;top:18px;font-size:31px;font-weight:700}
.nav-links{left:331px;top:31px;display:flex;font-size:16px}
.nav-links span{margin-right:27px}

.hero{left:0;top:78px;width:1200px;height:352px;
  background:radial-gradient(ellipse at 30% 40%,#b67a3e 0%,#7d5a44 35%,#4a4650 70%,#3c3f4c 100%)}
.podium-photo{left:35px;top:78px;width:275px;height:283px;
  background:linear-gradient(180deg,#9a6a45 0%,#d0541f 55%,#4a4a4e 78%,#3a3a3e 100%);opacity:.92}
.script-title{left:338px;top:92px;font-family:'Great Vibes',cursive;font-size:58px;color:var(--white)}
.tile{width:163px;height:68px;background:var(--tile-bg);border:1px solid var(--tile-border);border-radius:5px;
  text-align:center;line-height:1}
.tile .lead{display:block;font-size:21px;margin-top:6px}
.tile .role{display:block;font-size:31px;font-weight:700;margin-top:4px}
.tile.wide{width:187px}

.side-thumb{width:65px;height:70px;background:linear-gradient(180deg,#6b5a4e,#2d2622)}
.side-thumb.flag{background:linear-gradient(180deg,#6c7890,#b9b4a8)}
.side-title{font-size:18px;font-weight:900;line-height:19px}
.side-text{font-size:14px;font-weight:700;line-height:15.5px}

.feature-band{left:0;top:361px;width:1200px;height:69px;background:var(--band-bg)}
.dash-box{border:1.5px dashed var(--white);border-radius:7px}
.featured-label{left:92px;top:374px;width:161px;height:35px;font-size:23px;font-weight:900;text-align:center;line-height:32px}
.outlet{top:378px;height:28px;display:flex;align-items:center;justify-content:center;text-align:center;
  font-size:12px;font-weight:700;line-height:13px;color:var(--white)}
.follow-box{left:804px;top:374px;width:375px;height:35px}
.follow-label{left:810px;top:377px;font-size:13px;font-weight:900;line-height:13px;text-align:right;width:120px}
.social-sq{top:384px;width:14px;height:14px;background:var(--white)}
.email{left:1009px;top:382px;font-size:13.5px;font-weight:700}

.content-card{left:200px;top:442px;width:802px;height:516px;background:var(--white)}
.rule{left:553px;top:468px;width:95px;height:2px;background:var(--accent-blue)}
.copy{left:253px;top:503px;width:335px;font-family:'Roboto',sans-serif;color:var(--body-ink)}
.copy h2{font-size:17px;font-weight:700;color:var(--ink);margin-bottom:11px}
.copy p{font-size:11.6px;line-height:17.4px;margin-bottom:15px}
.portrait{left:616px;top:502px;width:332px;height:456px;
  background:radial-gradient(ellipse at 50% 55%,#2d6f78 0%,#7f9ea0 30%,#f3f1ee 65%)}
</style>
</head>
<body>

<header class="site-nav abs">
  <div class="brand abs">Lori Mentaskel</div>
  <nav class="nav-links abs">
    <span>Home</span><span>Meet Lori</span><span>Speaker/Spokesperson</span><span>Podcast</span><span>Books</span><span>Work with Lori</span><span>Contact</span><span>Press</span>
  </nav>
</header>

<section class="hero abs" role="img" aria-label="Blurred warm-toned audience in a conference hall"></section>
<div class="podium-photo abs" role="img" aria-label="Speaker in an orange blouse standing at a grey podium"></div>

<div class="script-title abs">Lori Mentaskel</div>

<div class="tile abs" style="left:335px;top:171px"><span class="lead">Dynatmic</span><span class="role">Keynoter</span></div>
<div class="tile abs" style="left:515px;top:171px"><span class="lead">Motivating</span><span class="role">Speaker</span></div>
<div class="tile wide abs" style="left:697px;top:171px"><span class="lead">Influential</span><span class="role">Broadcaster</span></div>
<div class="tile abs" style="left:335px;top:266px"><span class="lead">Prolific</span><span class="role">Author</span></div>
<div class="tile abs" style="left:515px;top:266px"><span class="lead" style="margin-top:3px">Enteraining</span><span class="role">Blogger</span></div>
<div class="tile wide abs" style="left:697px;top:266px"><span class="lead">Effective</span><span class="role">Trainer</span></div>

<div class="side-thumb abs" style="left:923px;top:128px" role="img" aria-label="Podcast guest portrait"></div>
<div class="side-title abs" style="left:998px;top:124px">OUR LATEST<br>PODCAST</div>
<div class="side-text abs" style="left:997px;top:165px">Podcast Guest:<br>Dana Whitcombe, NOVA<br>Season Brightway Radio,<br>July 26–Guest:<br>Dana Whitcombe, ...Click Here</div>

<div class="side-thumb flag abs" style="left:923px;top:268px" role="img" aria-label="Speaker portrait in front of a flag"></div>
<div class="side-title abs" style="left:998px;top:267px">SPEAKER/<br>SPOKESPERSON</div>
<div class="side-text abs" style="left:999px;top:311px">Topics &amp; Testimonials</div>

<div class="feature-band abs"></div>
<div class="featured-label dash-box abs">FEATURD ON</div>
<div class="outlet abs" style="left:268px;width:96px">Ledger Net</div>
<div class="outlet abs" style="left:388px;width:76px">The Marla<br>Show</div>
<div class="outlet abs" style="left:476px;width:52px">Trade<br>Talk</div>
<div class="outlet abs" style="left:542px;width:58px">KVRN<br>81AM</div>
<div class="outlet abs" style="left:612px;width:86px">KLOM 620AM</div>
<div class="outlet abs" style="left:718px;width:70px">Onward</div>

<div class="follow-box dash-box abs"></div>
<div class="follow-label abs">FOLLOW US<br>ON SOCIAL MEDIA</div>
<div class="social-sq abs" style="left:938px"></div>
<div class="social-sq abs" style="left:962px;border-radius:50%"></div>
<div class="social-sq abs" style="left:986px"></div>
<div class="email abs">lorimentaskel@mailbox.me</div>

<main class="content-card abs"></main>
<div class="rule abs"></div>
<article class="copy abs">
  <h2>Influence &amp; Entertain</h2>
  <p>Lori Mentaskel is a keynote speaker, spokesperson, writer and consultant on longevity, successful aging, and the Boomer and Mature Markets.</p>
  <p>She shares her passion and advocacy through multiple media channels and is a highly sought-after business development and inspirational keynote speaker.</p>
  <p>Staff Training, Design, Marketing, Branding to Reach Boomers, the Mature, and Caregivers</p>
  <p>Do you want to increase your ROI in the boomer mature or caregiver markets? Discover the art and science of Lensing.</p>
  <p>Do you want to create a state-of-the-art adult facility, inside and out? Discover Hearthplan, Lori’s consortium of architects, landscape architects and ROI specialists.</p>
  <p>Do you want to expand your financial practice into the mature and boomer markets? Discover Financial Gerontology and empower your advisors.</p>
  <p>Here are just some of Lori’s Clients:</p>
</article>
<div class="portrait abs" role="img" aria-label="Seated portrait of the speaker in a teal dress on a black chair against a white backdrop"></div>

</body>
</html>
```